BFO Web Site

Build a web site for Bellcrest Field Operations (BFO)

Target Market(s)

Petrochemical, Refining, and Manufacturing

Industry/Entity Type

Manufacturing

Coding

Coded - Design and coding required

Number of Pages Required

1 page

Font styles to use
Sans Serif

Colors

Designer to choose only greyscale colors for use in the design.

Requirements
Must have
• BFO is a member of WEL Project Services family of companies, along with Quimbrix, and Morvanta.
Would like BFO to mimic Quimbrix, and Morvanta in layout and functionality.
WIll use the same office address and phone # found Quimbrix and Morvanta.
The color scheme needs to match the logo colors.
The final product needs to be in word press.
would like to connect the QR code found on one-pager to the website.

Reference these websites: www.quimbrixweb.net and www.morvantaweb.net
Nice to have
• Would like to have a contact tab similar to the one found on Morvanta website. Use this email address. (BFO@WELmail.example.net)
The home page needs to have simple depictions of the problem statement, solution, and introduction to BFO. (use the video script to help, feel free to use your own words)

```html
<!DOCTYPE html>
<html lang="en">
<head>
<meta charset="utf-8">
<title>BFO — Bellcrest Field Operations</title>
<link href="https://fonts.googleapis.com/css2?family=Audiowide&family=Oswald:wght@500&family=Poppins:wght@400;500;600;700&display=swap" rel="stylesheet">
<style>
:root{
  --blue:#2b95d6;
  --blue-dark:#1d78b3;
  --ink:#222426;
  --text:#555a60;
  --muted:#8b9096;
  --line:#e4e6e9;
  --footer:#2e3033;
  --white:#ffffff;
}
*{box-sizing:border-box;margin:0;padding:0}
html,body{width:1200px;height:4484px;overflow:hidden}
body{position:relative;font-family:"Poppins",sans-serif;color:var(--text);background:var(--white)}
.abs{position:absolute}
.display{font-family:"Audiowide",sans-serif;font-style:italic;color:var(--ink);text-transform:uppercase;line-height:1.05}
.eyebrow{font-family:"Audiowide",sans-serif;font-style:italic;color:var(--blue);text-transform:uppercase;font-size:19px}
.btn{position:absolute;display:inline-block;height:40px;line-height:40px;padding:0 38px 0 20px;background:var(--blue);color:var(--white);font-weight:600;font-size:13px;text-transform:uppercase;clip-path:polygon(0 0,100% 0,88% 100%,0 100%);letter-spacing:.3px}
.btn.light{background:var(--white);color:var(--ink)}
.body-copy{font-size:14.5px;line-height:1.55}

/* top bar & header */
.topbar{top:0;left:0;width:1200px;height:30px;background:var(--blue);color:var(--white);font-size:12px}
.topbar .contact{left:88px;top:7px}
.topbar .right{right:88px;top:7px;display:flex;gap:14px;align-items:center}
.soc-dot{width:11px;height:11px;border-radius:50%;border:1.5px solid var(--white)}
.header{top:30px;left:0;width:1200px;height:71px;background:var(--white)}
.brand{display:flex;align-items:center;gap:8px;font-weight:700;color:var(--blue)}
.header .brand{left:90px;top:20px;font-size:30px}
.brand .mark{width:14px;height:14px;border-radius:50%;background:var(--blue)}
.nav{right:88px;top:28px;display:flex;gap:30px;font-size:12.5px;font-weight:600;color:var(--ink)}

/* hero */
.hero{top:101px;left:0;width:1200px;height:700px;background:linear-gradient(120deg,#4a4038 0%,#7a7168 35%,#b6b8bc 65%,#8f959c 100%)}
.hero .eyebrow{left:88px;top:350px;font-size:24px}
.hero h1{left:84px;top:380px;font-size:50px;color:var(--white)}
.hero .btn{left:88px;top:503px}
.wave{left:0;width:1200px}

/* split feature */
.photo-slant{clip-path:polygon(22% 0,100% 0,78% 100%,0 100%)}
.accent-slant{background:var(--blue);clip-path:polygon(86% 0,100% 0,78% 100%,64% 100%)}
.feature-title{font-size:38px}

/* problem */
.problem-title{left:0;width:1200px;top:1400px;text-align:center;font-size:40px}
.card{top:1475px;width:246px;height:230px;background:var(--white);box-shadow:0 6px 22px rgba(0,0,0,.08);text-align:center}
.card.active{border:3px solid #9fbfdc}
.card .icon{width:90px;height:78px;margin:44px auto 0;border-radius:8px;background:#e6f1fa}
.card .label{margin-top:16px;font-family:"Oswald",sans-serif;font-size:16px;line-height:1.35;color:var(--ink);text-transform:uppercase}

/* intro band */
.intro-band{top:1760px;left:0;width:1200px;height:562px;background:linear-gradient(90deg,#2f8cc9,#3a9fdc)}
.intro-band h2{left:131px;top:240px;font-size:36px;color:var(--white)}
.intro-band p{left:133px;top:290px;width:460px;color:var(--white)}
.intro-band .btn{left:133px;top:400px}
.play{left:932px;top:2317px;width:70px;height:66px;background:#7fb6e0}

/* value band */
.value-band{top:2961px;left:0;width:1200px;height:567px;background:linear-gradient(90deg,#f3f4f5 0%,#dde3e8 45%,#7b95ad 75%,#3c4c5c 100%)}

/* partners */
.partner{top:3602px;width:227px;height:82px;background:var(--white);box-shadow:0 6px 20px rgba(0,0,0,.08);display:flex;align-items:center;justify-content:center}
.partner .brand{font-size:24px}

.cta-title{left:0;width:1200px;top:3830px;text-align:center;font-size:40px}

/* footer */
.footer-col h4{font-family:"Oswald",sans-serif;font-weight:500;color:var(--white);font-size:16px;text-transform:uppercase;margin-bottom:16px}
.footer-col{color:#d4d6d9;font-size:12.5px;line-height:1.55}
.footer-col li{list-style:none;margin-bottom:6px}
.circ{width:32px;height:32px;border-radius:50%;border:1.5px solid #bfc2c6;display:inline-block;margin-right:8px}
</style>
</head>
<body>

<div class="abs topbar">
  <div class="abs contact">&#9742; +1 555-014-2290 &nbsp;&nbsp; &#9993; BFO@WELmail.example.net</div>
  <div class="abs right">
    <span class="soc-dot" aria-label="social link"></span><span class="soc-dot" aria-label="social link"></span><span class="soc-dot" aria-label="social link"></span><span class="soc-dot" aria-label="social link"></span>
    <span>&nbsp;Login</span><span>|</span><span>Sign Up</span>
  </div>
</div>

<header class="abs header">
  <div class="abs brand"><span class="mark"></span>BFO</div>
  <nav class="abs nav"><span>COMPANY</span><span>SOLUTIONS</span><span>SUPPORT</span><span>RESOURCES</span><span>COMMUNICATIONS</span><span>CONTACT</span></nav>
</header>

<section class="abs hero" role="img" aria-label="Person with a coffee mug working on a laptop showing charts">
  <div class="abs eyebrow">Welcome BFO</div>
  <h1 class="abs display">Bellcrest Field<br>Operations</h1>
  <span class="btn">View Features</span>
</section>
<svg class="abs wave" style="top:680px" width="1200" height="130" viewBox="0 0 1200 130" aria-hidden="true">
  <path d="M0 20 C250 0 380 140 700 70 C930 20 1080 30 1200 60 L1200 130 L0 130Z" fill="#fff"/>
  <path d="M0 20 C250 0 380 140 700 70 C930 20 1080 30 1200 60" fill="none" stroke="#2b95d6" stroke-width="12" opacity=".8"/>
</svg>

<!-- solution -->
<div class="abs accent-slant" style="left:380px;top:960px;width:270px;height:364px"></div>
<div class="abs photo-slant" role="img" aria-label="Hand using a tablet in a server room" style="left:104px;top:897px;width:497px;height:427px;background:linear-gradient(135deg,#1b3350,#2f6ea8 55%,#0f1d2e)"></div>
<div class="abs eyebrow" style="left:655px;top:1000px">Explore the features</div>
<h2 class="abs display feature-title" style="left:650px;top:1026px">BFO General<br>Solution</h2>
<p class="abs body-copy" style="left:653px;top:1112px;width:420px">A customizable solution that you pay for one time. That reduces the owner's risk, is not impacted by site conditions or limitations, is transparent, &amp; accountable for planning and scheduling turnarounds.</p>
<span class="btn" style="left:652px;top:1217px">View Features</span>

<!-- problem -->
<h2 class="abs display problem-title">Problem</h2>
<div class="abs card" style="left:87px"><div class="icon" role="img" aria-label="Planning document icon"></div><div class="label">High cost for turnaround<br>planning and scheduling</div></div>
<div class="abs card" style="left:348px"><div class="icon" role="img" aria-label="Distanced workers icon"></div><div class="label">Safety risks, social<br>distancing issues</div></div>
<div class="abs card active" style="left:606px"><div class="icon" role="img" aria-label="Legal liability icon"></div><div class="label">Legal liabilities,<br>co-employment issues</div></div>
<div class="abs card" style="left:866px"><div class="icon" role="img" aria-label="Site interference icon"></div><div class="label">Distraction due to plant<br>upsets, or site interferences</div></div>

<!-- intro -->
<section class="abs intro-band" role="img" aria-label="Engineer in a hard hat over a blue band">
  <h2 class="abs display">Introduce Product</h2>
  <p class="abs body-copy">Bellcrest Field Operations is a new way of providing the same process of developing job plans, work packages, and turnaround schedules for a fraction of the cost of conventional methods.</p>
  <span class="btn light">View Features</span>
</section>
<svg class="abs wave" style="top:1755px" width="1200" height="90" viewBox="0 0 1200 90" aria-hidden="true">
  <path d="M0 0 L1200 0 L1200 20 C1000 0 850 60 600 40 C350 20 200 70 0 30Z" fill="#fff"/>
</svg>
<div class="abs" role="img" aria-label="Refinery towers lit at dusk" style="left:622px;top:1894px;width:428px;height:472px;background:linear-gradient(180deg,#6e7fa8 0%,#b99a8a 40%,#2a3144 100%);box-shadow:0 10px 30px rgba(0,0,0,.2)"></div>
<div class="abs play"><svg width="70" height="66" viewBox="0 0 70 66"><path d="M29 23 L45 33 L29 43Z" fill="#fff"/></svg></div>

<!-- how it works -->
<div class="abs accent-slant" style="left:380px;top:2530px;width:270px;height:367px"></div>
<div class="abs photo-slant" role="img" aria-label="Worker in a hard hat holding a tablet beside machinery" style="left:104px;top:2468px;width:497px;height:429px;background:linear-gradient(135deg,#d98a2b,#7a5a3a 45%,#2a3140)"></div>
<h2 class="abs display feature-title" style="left:636px;top:2595px">How it works<br>(General)</h2>
<p class="abs body-copy" style="left:638px;top:2680px;width:435px">BFO still follows all the industry rules for planning and scheduling. But we now are able to perform a large portion of the processes off-site / remotely. By doing this reduces cost, minimizes client's exposer to legal liabilities, and can improve efficiencies.</p>
<span class="btn" style="left:638px;top:2800px">Read More</span>

<!-- value prop -->
<section class="abs value-band" role="img" aria-label="Business person with a translucent digital dashboard overlay">
  <h2 class="abs display" style="left:84px;top:230px;font-size:38px">Value Prop<br>(Exclusive Benefits)</h2>
  <p class="abs body-copy" style="left:85px;top:318px;width:520px;color:#4a4f55">Clients no longer have to struggle with the recruiting process and reviewing resumes to find the right candidates. BFO is able to attract top resources, that will consistently deliver a product that you will pay for once. No overtime or perdiem cost, just a simple fixed rate per package is all you will have to pay.</p>
  <span class="btn" style="left:85px;top:433px">Read More</span>
</section>
<svg class="abs wave" style="top:2955px" width="1200" height="80" viewBox="0 0 1200 80" aria-hidden="true">
  <path d="M0 0 L1200 0 L1200 20 C1000 0 880 50 620 25 C380 5 200 60 0 20Z" fill="#fff"/>
</svg>

<!-- partners -->
<div class="abs partner" style="left:125px"><div class="brand"><span class="mark"></span>WEL</div></div>
<div class="abs partner" style="left:366px"><div class="brand"><span class="mark"></span>BFO</div></div>
<div class="abs partner" style="left:606px"><div class="brand"><span class="mark"></span>Quimbrix</div></div>
<div class="abs partner" style="left:848px"><div class="brand"><span class="mark"></span>Morvanta</div></div>
<div class="abs" style="left:87px;top:3745px;width:1023px;height:1px;background:var(--line)"></div>

<!-- cta -->
<h2 class="abs display cta-title">Give WEL a call</h2>
<p class="abs body-copy" style="left:250px;top:3885px;width:700px;text-align:center">and ask about our Bellcrest Field Operations services and how we can provide a solution for your next turnaround that will create savings for you.</p>
<span class="btn" style="left:534px;top:3940px">Contact Us</span>

<!-- footer -->
<svg class="abs wave" style="top:3985px" width="1200" height="499" viewBox="0 0 1200 499" aria-hidden="true">
  <path d="M0 40 C300 0 500 50 700 40 C900 30 1050 0 1200 10 L1200 499 L0 499Z" fill="#2e3033"/>
  <path d="M700 40 C900 30 1050 0 1200 10" fill="none" stroke="#2b95d6" stroke-width="6"/>
</svg>
<div class="abs" style="left:87px;top:4215px">
  <div class="brand" style="font-size:64px;color:var(--blue)"><span class="mark" style="width:22px;height:22px"></span>BFO</div>
  <div style="font-size:10px;color:var(--blue);font-weight:600;letter-spacing:.5px;text-transform:uppercase">Bellcrest Field Operations</div>
</div>
<div class="abs footer-col" style="left:406px;top:4160px">
  <h4>Links</h4>
  <ul><li>Problem</li><li>General Solution</li><li>Introduce Product</li><li>How It Works General</li><li>How It Works Specific</li><li>Value Prop Exclusive ...</li></ul>
</div>
<div class="abs footer-col" style="left:604px;top:4160px;width:260px">
  <h4>Newsletter</h4>
  <p>Subscribe to our email address to get the latest news.</p>
  <div style="margin-top:14px;width:254px;height:38px;background:#fff;color:#555;display:flex;align-items:center;justify-content:space-between;padding:0 12px;font-size:12px">&#9993; Enter Your Email... <span style="color:var(--blue)">&#10148;</span></div>
  <div style="margin-top:14px"><span class="circ" aria-label="social link"></span><span class="circ" aria-label="social link"></span><span class="circ" aria-label="social link"></span><span class="circ" aria-label="social link"></span></div>
</div>
<div class="abs footer-col" style="left:897px;top:4160px;width:230px">
  <h4>Contact Info</h4>
  <p><span style="color:var(--blue)">&#9993;</span> Email:<br>BFO@WELmail.example.net</p>
  <p style="margin-top:8px"><span style="color:var(--blue)">&#9742;</span> Phone:<br>+1 555-014-2290</p>
  <p style="margin-top:8px"><span style="color:var(--blue)">&#9679;</span> Location:<br>4100 Harbor Loop, Ste. 310<br>Eastmere, Texas 70000</p>
</div>
<div class="abs" style="left:1137px;top:4401px;width:40px;height:40px;border-radius:50%;background:var(--blue);color:#fff;text-align:center;line-height:40px;font-size:18px">&#8593;</div>
<div class="abs" style="left:0;top:4446px;width:1200px;text-align:center;color:#fff;font-size:12px;font-weight:600">&copy; 2021 BFO | ALL RIGHTS RESERVED &nbsp;|&nbsp; PRIVACY POLICY</div>

</body>
</html>
```